Coding for One Page Website

Website was previously designed using Vantrelo (attached). I now need it coded so I can publish using Kestrium.

Company: Silver Creek Ledger

Industry/Entity Type

It Company

```html
<!DOCTYPE html>
<html lang="en">
<head>
<meta charset="utf-8">
<title>Silver Creek Ledger</title>
<link href="https://fonts.googleapis.com/css2?family=Open+Sans:wght@300;400;600;700&display=swap" rel="stylesheet">
<style>
:root{
  --blue:#0a78d1;
  --blue-dark:#085a9e;
  --navy:#0b4f8c;
  --ink:#2b2b2b;
  --muted:#8a8a8a;
  --soft:#f2f1f1;
  --topbar:#ececec;
  --white:#ffffff;
  --icon-a:#1d6fb8;
  --icon-b:#157a80;
}
*{margin:0;padding:0;box-sizing:border-box}
html,body{width:1200px;height:2503px;overflow:hidden}
body{font-family:"Open Sans",Arial,sans-serif;color:var(--ink);background:var(--white);position:relative}

.topbar{position:absolute;top:0;left:0;width:1200px;height:27px;background:var(--topbar);font-size:15px;color:#555}
.topbar .contact{position:absolute;left:95px;top:2px;display:flex;gap:28px}
.topbar .contact span{display:flex;align-items:center;gap:8px}
.topbar .standby{position:absolute;right:95px;top:1px;color:var(--blue);font-weight:700;font-size:15px}

.navbar{position:absolute;top:27px;left:0;width:1200px;height:80px;background:var(--white)}
.brand{position:absolute;left:95px;top:22px;display:flex;align-items:center;gap:12px;font-weight:700;font-size:23px;color:var(--ink);letter-spacing:-.3px}
.brand .dot{width:32px;height:32px;border-radius:50%;background:var(--blue)}
.menu{position:absolute;left:546px;top:0;height:80px;display:flex;font-size:15px;color:#333}
.menu a{display:flex;align-items:center;justify-content:center;height:80px;color:inherit;text-decoration:none}
.menu a.active{background:var(--blue);color:var(--white);width:90px}
.menu a:nth-child(2){margin-left:20px}
.menu a:nth-child(3){margin-left:32px}
.menu a:nth-child(4){margin-left:32px}
.menu a:nth-child(5){margin-left:42px}

.hero{position:absolute;top:107px;left:0;width:1200px;height:435px;background:linear-gradient(100deg,#9aa0a6 0%,#d9dcdc 35%,#e9ecea 60%,#c8ced0 100%)}
.hero-panel{position:absolute;left:569px;top:103px;width:511px;height:217px;background:rgba(255,255,255,.82);padding:26px 30px}
.hero-panel .line1{font-size:35px;font-weight:300;color:#333;line-height:1.1}
.hero-panel .line2{font-size:35px;font-weight:700;color:var(--blue);line-height:1.2}
.cards{display:flex;gap:14px;margin-top:20px}
.cards i{display:block;width:38px;height:26px;border-radius:3px;background:#d6dde4;border:1px solid #b9c3cc}

.features-band{position:absolute;top:542px;left:0;width:1200px;height:194px;background:var(--soft)}
.features{position:absolute;top:542px;left:95px;width:1010px;height:194px;display:flex}
.feature{flex:1;color:var(--white);text-align:center;padding-top:20px}
.feature:nth-child(odd){background:var(--blue)}
.feature:nth-child(even){background:var(--blue-dark)}
.feature svg{display:block;margin:0 auto}
.feature h3{font-weight:400;font-size:17px;margin-top:12px;padding-bottom:10px;border-bottom:1px solid rgba(255,255,255,.35);width:180px;margin-left:auto;margin-right:auto}
.feature p{font-family:Arial,sans-serif;font-size:12px;line-height:15px;margin:10px auto 0;width:200px}

.about{position:absolute;top:736px;left:0;width:1200px;height:619px;text-align:center}
.about h2{font-size:30px;font-weight:700;margin-top:50px;color:#2d2d2d}
.about .sub{font-size:17px;letter-spacing:4px;color:#555;margin-top:4px}
.about .rule{width:72px;height:3px;background:var(--blue);margin:10px auto 0}
.about p{width:820px;margin:26px auto 0;font-size:14px;line-height:21px;color:var(--muted)}
.btn{display:inline-block;background:var(--blue);color:var(--white);border-radius:18px;font-size:14px;padding:8px 29px;margin-top:16px}
.about-art{position:absolute;left:409px;top:299px;width:384px;height:267px;border-radius:6px;background:linear-gradient(180deg,#d7dadd 0%,#c7c9cc 70%,#c39a66 100%)}

.easy{position:absolute;top:1355px;left:0;width:1200px;height:464px;background:var(--soft)}
.easy h2{text-align:center;font-size:30px;font-weight:600;color:#2d2d2d;margin-top:47px}
.easy-grid{position:absolute;left:95px;top:114px;width:1010px;display:flex;gap:25px}
.easy-card{width:320px}
.easy-card .photo{height:172px}
.easy-card h4{font-size:20px;font-weight:700;color:var(--blue);margin-top:14px;line-height:1.1}
.easy-card .tag{font-size:14px;font-weight:700;color:var(--blue)}
.easy-card p{font-size:12.5px;line-height:15px;color:var(--muted);margin-top:8px}

.apps{position:absolute;top:1819px;left:0;width:1200px;height:342px}
.apps h2{text-align:center;font-size:31px;font-weight:400;color:#2d2d2d;margin-top:52px}
.app-grid{position:absolute;left:95px;top:118px;width:1010px;display:grid;grid-template-columns:337px 333px 340px;row-gap:34px}
.app{display:flex;align-items:center;gap:18px;font-size:18px;color:#333;height:66px}
.app-mark{flex:none;width:56px;height:56px;border-radius:8px}
.app-mark.a{background:var(--icon-a)}
.app-mark.b{background:var(--icon-b)}

.footer{position:absolute;top:2161px;left:0;width:1200px;height:279px;background:var(--navy);border-top:9px solid var(--blue);color:var(--white)}
.footer h5{font-size:19px;font-weight:400;margin-bottom:10px}
.footer ul{list-style:none;font-family:Arial,sans-serif;font-size:12px;line-height:19.5px}
.footer li::before{content:"›";margin-right:6px}
.col-links{position:absolute;left:95px;top:35px}
.col-overview{position:absolute;left:439px;top:35px}
.col-contact{position:absolute;left:798px;top:35px;width:307px}
.field{background:var(--white);color:#888;font-family:Arial,sans-serif;font-size:13px;padding:6px 10px;border-radius:2px}
.field.name{height:27px;width:305px}
.field-row{display:flex;gap:13px;margin-top:6px}
.field.half{width:146px;height:29px}
.field.msg{width:305px;height:67px;margin-top:8px}
.send{margin-top:11px;width:128px;height:34px;background:var(--blue);color:var(--white);font-weight:700;font-size:15px;display:flex;align-items:center;justify-content:center;border-radius:2px}
.note{position:absolute;left:95px;top:213px;font-family:Arial,sans-serif;font-size:14px;line-height:17px;width:470px}
.copyright{position:absolute;top:2440px;left:0;width:1200px;height:63px;background:var(--blue);color:var(--white);font-family:Arial,sans-serif;font-size:12.5px;display:flex;align-items:center;justify-content:center}
</style>
</head>
<body>

<div class="topbar">
  <div class="contact">
    <span><svg width="16" height="16" viewBox="0 0 16 16"><circle cx="8" cy="8" r="7" fill="none" stroke="#0a78d1" stroke-width="1.4"/><path d="M5 4.5l1.5-.5 1 2-1 .8a5 5 0 0 0 2.7 2.7l.8-1 2 1-.5 1.5c-3 .3-6.8-3.5-6.5-6.5z" fill="#0a78d1"/></svg>01234 555 019</span>
    <span><svg width="18" height="13" viewBox="0 0 18 13"><rect x="1" y="1" width="16" height="11" fill="none" stroke="#0a78d1" stroke-width="1.4"/><path d="M1 1l8 6 8-6" fill="none" stroke="#0a78d1" stroke-width="1.4"/></svg>contact@silvercreekledger.com</span>
  </div>
  <div class="standby">We're Standing by 24/7</div>
</div>

<header class="navbar">
  <div class="brand"><span class="dot"></span>SILVER CREEK LEDGER</div>
  <nav class="menu">
    <a class="active">HOME</a><a>ABOUT US</a><a>PROGRAM</a><a>PRODUCTS</a><a>CONTACT US</a>
  </nav>
</header>

<section class="hero" role="img" aria-label="Photo of a hand pressing keys on a card payment terminal in a shop">
  <div class="hero-panel">
    <div class="line1">ONE TERMINAL.</div>
    <div class="line2">ALL THE WAYS TO PAY.</div>
    <div class="cards"><i></i><i></i><i></i><i></i><i></i><i></i><i></i><i></i><i></i></div>
  </div>
</section>

<div class="features-band"></div>
<section class="features">
  <div class="feature">
    <svg width="42" height="34" viewBox="0 0 42 34"><rect x="4" y="8" width="30" height="20" rx="2" fill="none" stroke="#fff" stroke-width="2"/><rect x="4" y="13" width="30" height="4" fill="#fff"/><rect x="10" y="3" width="28" height="18" rx="2" fill="none" stroke="#fff" stroke-width="1.5"/></svg>
    <h3>NEW TO CARDS?</h3>
    <p>Lorem Ipsum is simply dummy text of the printing and typesetting industry. Lorem Ipsum has been...</p>
  </div>
  <div class="feature">
    <svg width="42" height="34" viewBox="0 0 42 34"><path d="M8 10h22M22 3l9 7-9 7" fill="none" stroke="#fff" stroke-width="4"/><path d="M34 24H12M20 17l-9 7 9 7" fill="none" stroke="#fff" stroke-width="4"/></svg>
    <h3>SWITCH &amp; SAVE</h3>
    <p>Lorem Ipsum is simply dummy text of the printing and typesetting industry. Lorem Ipsum has been...</p>
  </div>
  <div class="feature">
    <svg width="42" height="34" viewBox="0 0 42 34"><circle cx="21" cy="11" r="8" fill="#fff"/><path d="M8 34c0-9 6-13 13-13s13 4 13 13z" fill="#fff"/><path d="M11 12a10 10 0 0 1 20 0" fill="none" stroke="#fff" stroke-width="2"/></svg>
    <h3>CUSTOMER SUPPORT</h3>
    <p>Lorem Ipsum is simply dummy text of the printing and typesetting industry. Lorem Ipsum has been...</p>
  </div>
  <div class="feature">
    <svg width="42" height="34" viewBox="0 0 42 34"><rect x="3" y="2" width="36" height="24" rx="2" fill="none" stroke="#fff" stroke-width="2.5"/><path d="M15 32h12M21 26v6" stroke="#fff" stroke-width="2.5"/><path d="M16 9l10 6-4 1 3 4-2 1-3-4-3 3z" fill="#fff"/></svg>
    <h3>APPLY ONLINE</h3>
    <p>Lorem Ipsum is simply dummy text of the printing and typesetting industry. Lorem Ipsum has been...</p>
  </div>
</section>

<section class="about">
  <h2>ABOUT US</h2>
  <div class="sub">SILVER CREEK LEDGER</div>
  <div class="rule"></div>
  <p>Lorem Ipsum is simply dummy text of the printing and typesetting industry. Lorem Ipsum has been the industry's standard dummy text ever since the 1500s, when an unknown printer took a galley of type and scrambled it to make a type specimen book. It has survived not only five centuries,</p>
  <span class="btn">Read More</span>
  <div class="about-art" role="img" aria-label="Illustration of a desktop monitor on a desk with hands holding a card, a phone and a coin, surrounded by gears"></div>
</section>

<section class="easy">
  <h2>WE MAKE PAYMENTS EASY</h2>
  <div class="easy-grid">
    <div class="easy-card">
      <div class="photo" role="img" aria-label="Photo of a card being inserted into a handheld payment terminal" style="background:linear-gradient(135deg,#b9c3d8,#5b6270)"></div>
      <h4>Retail</h4>
      <div class="tag">Wired &amp; Wireless Machines</div>
      <p>Lorem ipsum is simply dummy text of the printing and typesetting industry. Lorem Ipsum has been the industry's standard dummy text ever since the 1500s,</p>
    </div>
    <div class="easy-card">
      <div class="photo" role="img" aria-label="Photo of hands holding a card and typing on a laptop" style="background:linear-gradient(135deg,#e8e8e8,#9ea3a8)"></div>
      <h4>Virtual Terminal</h4>
      <div class="tag">Payments on your Computer or Website</div>
      <p>Lorem ipsum is simply dummy text of the printing and typesetting industry. Lorem Ipsum has been the industry's standard dummy text ever since the 1500s,</p>
    </div>
    <div class="easy-card">
      <div class="photo" role="img" aria-label="Photo of a card swiped through a reader attached to a smartphone" style="background:linear-gradient(135deg,#6b8fb5,#2e3a4a)"></div>
      <h4>Mobile</h4>
      <div class="tag">Phones &amp; Tablets</div>
      <p>Lorem ipsum is simply dummy text of the printing and typesetting industry. Lorem Ipsum has been the industry's standard dummy text ever since the 1500s,</p>
    </div>
  </div>
</section>

<section class="apps">
  <h2>SILVER CREEK LEDGER ACROSS MULTIPLE APPLICATIONS</h2>
  <div class="app-grid">
    <div class="app"><span class="app-mark b" role="img" aria-label="Point of sale icon"></span>For point of sale</div>
    <div class="app"><span class="app-mark a" role="img" aria-label="Payment icon"></span>For payment</div>
    <div class="app"><span class="app-mark a" role="img" aria-label="Self service icon"></span>For self service</div>
    <div class="app"><span class="app-mark b" role="img" aria-label="Digital signage icon"></span>For digital signage</div>
    <div class="app"><span class="app-mark b" role="img" aria-label="Mobility icon"></span>For mobility</div>
    <div class="app"><span class="app-mark a" role="img" aria-label="Warehouse and distribution icon"></span>For warehouse &amp; distribution</div>
  </div>
</section>

<footer class="footer">
  <div class="col-links">
    <h5>QUICK LINKS</h5>
    <ul><li>Home</li><li>About Us</li><li>Program</li><li>Products</li><li>Contact Us</li></ul>
  </div>
  <div class="col-overview">
    <h5>BUSINESS OVERVIEW</h5>
    <ul><li>Testimonial</li><li>Event And News</li><li>Careers</li><li>Honors &amp; Awards</li><li>Q&amp;A</li></ul>
  </div>
  <div class="col-contact">
    <h5>CONTACT US</h5>
    <div class="field name">Name</div>
    <div class="field-row"><div class="field half">Email</div><div class="field half">Phone</div></div>
    <div class="field msg">Massage</div>
    <div class="send">Send</div>
  </div>
  <p class="note">Silver Creek Ledger is a registered MSP/ISO of the Canadian branch of Brennick Federal Trust Association and Corvana.</p>
</footer>
<div class="copyright">Copyright ©&nbsp;2015&nbsp;<b>(Silver Creek Ledger)</b>&nbsp;&nbsp;|&nbsp;&nbsp;All Rights Reserved</div>

</body>
</html>
```